Flyer für Tiertherapeutin
Eine sehr motivierte und kreative Designerin. Schon der erste Vorschlag war ganz nach meinen Vorstellungen.
Zielgruppe
Ich bin Tiertherapeutin für TCVM und Ernährungsberaterin für Hunde und Katzen. Mittels Akupunktur, Lasertherapie, Mykotherapie und Ernährungsberatung kommt es zu einer Linderung vorhandener Schmerzen, eine verbesserte Regulation der Organe und einer Steigerung das Wohlbefindens sowie Lebensqualität.
Zielgruppe sind überwiegend weibliche Hunde- und Katzenbesitzer mit erkrankten Tieren.
Aufgabenstellung
Flyer sollte klappbar sein. Logo und mein Name und Kontaktdaten sollten enthalten sein.

```html
<!DOCTYPE html>
<html lang="de">
<head>
<meta charset="utf-8">
<title>Flyer Tiertherapie – Innenseite</title>
<link href="https://fonts.googleapis.com/css2?family=Open+Sans:wght@400&family=Cookie&display=swap" rel="stylesheet">
<style>
  :root {
    --band: #d09a68;
    --band-dark: #4a3f30;
    --heading: #c8925e;
    --text: #2a2a2a;
    --box: #eceef2;
    --paper: #ffffff;
  }
  * { box-sizing: border-box; margin: 0; padding: 0; }
  html, body { width: 1200px; height: 848px; overflow: hidden; background: var(--paper); }
  body {
    position: relative;
    font-family: "Open Sans", Arial, sans-serif;
    color: var(--text);
    font-size: 12.3px;
  }
  .top-band { position: absolute; left: 0; top: 0; width: 1200px; height: 230px; }
  .portrait {
    position: absolute; left: 160px; top: 40px; width: 262px; height: 262px;
    border-radius: 50%; border: 7px solid var(--paper);
    background: radial-gradient(circle at 55% 40%, #e8d3b8 0%, #b5a68f 35%, #2d3350 70%, #ded8d2 100%);
  }
  .pet-photo {
    position: absolute; left: 282px; top: 580px; width: 350px; height: 350px;
    border-radius: 50%;
    background: radial-gradient(circle at 45% 55%, #c08a58 0%, #b07a4d 40%, #8a6a55 70%, #b7a89a 100%);
  }
  .script-title {
    position: absolute; font-family: "Cookie", cursive; color: var(--heading);
    font-size: 40px; line-height: 1; font-weight: 400;
  }
  .title-hello { left: 40px; top: 264px; }
  .title-tcm { left: 442px; top: 268px; }

  .column { position: absolute; top: 318px; width: 331px; }
  .col-about { left: 42px; line-height: 21.3px; }
  .col-tcm { left: 443px; line-height: 20px; }
  .col-uses { left: 837px; line-height: 20px; }
  .para { margin-bottom: 21.3px; }
  .col-tcm .para { margin-bottom: 20px; }
  .line { display: block; text-align: justify; text-align-last: justify; white-space: nowrap; }
  .line.end { text-align-last: left; }
  .spread { letter-spacing: 2.4px; }

  .uses-intro { margin-bottom: 10px; }
  .uses-box {
    background: var(--box); border-radius: 14px;
    width: 331px; height: 436px; padding: 16px 18px 0 10px;
  }
  .uses-box ul { list-style: none; font-size: 11.3px; line-height: 12.5px; }
  .uses-box li { position: relative; padding-left: 25px; margin-bottom: 7.3px; text-align: justify; }
  .uses-box li::before { content: "•"; position: absolute; left: 0; top: 0; }
</style>
</head>
<body>
  <svg class="top-band" viewBox="0 0 1200 230" aria-hidden="true">
    <path d="M0 0 H1200 V133 Q760 215 420 205 Q200 195 0 164 Z" fill="var(--band)"/>
    <path d="M0 178 Q200 205 420 215 Q760 225 1200 152 V166 Q760 235 420 222 Q200 212 0 188 Z" fill="var(--band-dark)"/>
  </svg>
  <div role="img" aria-label="Pfotenspuren als Dekoration" style="position:absolute;left:610px;top:0;width:410px;height:180px;"></div>

  <div class="portrait" role="img" aria-label="Porträtfoto der Therapeutin mit weißer Katze im Arm"></div>

  <h1 class="script-title title-hello">Hallo!</h1>
  <h2 class="script-title title-tcm">Was ist TCM?</h2>

  <section class="column col-about">
    <p class="para">
      <span class="line end">Mein Name ist Johanna Wendel.</span>
      <span class="line">Ich bin Tierernährungsberaterin für Hunde und Katzen,</span>
      <span class="line">Akupunkteurin (TCVM) für Hunde, Katzen und Pferde</span>
      <span class="line">und Katzenverhaltenstrainerin und somit in der optima-</span>
      <span class="line">len Lage, die Erkrankung deines Tieres umfassend zu</span>
      <span class="line end">betrachten und zu behandeln.</span>
    </p>
    <p class="para">
      <span class="line">Mein Ziel ist es, den Körper deines Tieres in ein inne-</span>
      <span class="line">res Gleichgewicht zu bringen, die Selbstheilungskräfte</span>
      <span class="line">zu aktivieren und dies führt zu einem schmerzfreien</span>
      <span class="line">und gesunden Leben deines besten Fellfreundes. Mei-</span>
      <span class="line">ne Therapiemethoden lindern nicht nur die Symptome,</span>
      <span class="line end">sondern lösen die Ursachen auf.</span>
    </p>
    <p class="para">
      <span class="line" style="width:277px">Während der Behandlung ist es mir wichtig,</span>
      <span class="line" style="width:259px">dass sich dein Tier entspannt. Das kann es</span>
      <span class="line" style="width:246px">im gewohnten Umfeld am besten. Daher</span>
      <span class="line" style="width:236px">arbeite ich mobil im Raum Karlsruhe</span>
      <span class="line end">und Umgebung.</span>
    </p>
  </section>

  <section class="column col-tcm">
    <p class="para">
      <span class="line">Die traditionelle chinesische Medizin für Tiere (TCVM) ist</span>
      <span class="line">ein ganzheitliches medizinisches System, das auf einer</span>
      <span class="line">jahrtausendealten chinesischen Tradition basiert. Sie</span>
      <span class="line">umfasst verschiedene Behandlungsmethoden wie Aku-</span>
      <span class="line">punktur, Moxibustion, Lasertherapie, Kräuterheilkunde,</span>
      <span class="line end">Ernährungstherapie und Tuina.</span>
    </p>
    <p class="para">
      <span class="line">Die TCVM betrachtet den tierischen Körper als ein kom-</span>
      <span class="line">plexes System, das von der Lebensenergie „Qi“ durch-</span>
      <span class="line">strömt wird. Krankheiten entstehen, wenn das Qi aus</span>
      <span class="line end">dem Gleichgewicht gerät oder blockiert ist.</span>
    </p>
    <p class="para">
      <span class="line" style="margin-left:68px">Ziel der TCVM ist es, die Energie (Qi) wieder</span>
      <span class="line" style="margin-left:117px">ins Gleichgewicht zu bringen und</span>
      <span class="line" style="margin-left:147px">die Selbstheilungskräfte des</span>
      <span class="line" style="margin-left:168px">Körpers zu aktivieren. Die</span>
      <span class="line" style="margin-left:183px">chinesische Diagnostik</span>
      <span class="line" style="margin-left:196px">ist sehr detaillierte</span>
      <span class="line" style="margin-left:205px">und aufwändig, um</span>
      <span class="line spread" style="margin-left:212px">krankmachende</span>
      <span class="line" style="margin-left:216px">Disharmonien zu</span>
      <span class="line" style="margin-left:217px">finden und diese</span>
      <span class="line end" style="margin-left:219px">zu entstören.</span>
    </p>
  </section>

  <div class="pet-photo" role="img" aria-label="Nahaufnahme eines Hundes mit Akupunkturnadeln im Fell"></div>

  <section class="column col-uses">
    <p class="uses-intro">Die TCM wird häufig zur Behandlung einer Vielzahl von Erkrankungen eingesetzt, darunter:</p>
    <div class="uses-box">
      <ul>
        <li>(chronische) Schmerzen</li>
        <li>Gelenkserkrankungen (HD, ED, OCD)</li>
        <li>Lähmungen, Nervenverletzungen, Verspannungen, Luxationen, Myositis, Bänderrisse</li>
        <li>Entzündliche Erkrankungen der Sehnen- und Seh&shy;nenscheiden</li>
        <li>Atemwegserkrankungen</li>
        <li>Immunschwäche, Infektanfälligkeit</li>
        <li>Gestörte Wundheilung, Narbenbehandlung</li>
        <li>Epilepsie</li>
        <li>Neuralgien</li>
        <li>Augen- und Ohrenerkrankungen</li>
        <li>Nieren- und Blasenerkrankungen (Harninkontinenz und Blasenentzündung)</li>
        <li>Entstörung von Narben</li>
        <li>Unruhen, Stress, Angst</li>
        <li>Juckreiz</li>
        <li>Verdauungsproblemen</li>
        <li>Allergien</li>
        <li>Altersbeschwerden (Schwäche, Erschöpfung)</li>
        <li>Hormonelle Erkrankungen/Störungen (z.B. Zyklus&shy;störungen)</li>
      </ul>
    </div>
  </section>
</body>
</html>
```